Flyer Design Project with menu

We are from Copperleaf Kitchen Restaurant. We usually serve breakfast, soul food, fried and BBQ Ribs , legs, wings etc. We located at 2738 n. Willow avenue, canton, 39046, MS. Since this is a new restaurant we want to let people know about us. Please create a good professional flyer including menu on that. Thank you. Please let us know if you need any other information.

Target Market(s)

We want to attract customers from 3 different locations near 15 miles radius.

Industry/Entity Type

American Restaurant

Font styles to use
Serif

Requirements
Must have
• Good graphics with food pictures.
• Soul food graphic pictures, RIBS, FISH and breakfast regular.
Nice to have
• 20% discount coupon offer.

```html
<!DOCTYPE html>
<html lang="en">
<head>
<meta charset="utf-8">
<title>Copperleaf Kitchen Restaurant – Menu Flyer</title>
<link href="https://fonts.googleapis.com/css2?family=Alfa+Slab+One&family=Zilla+Slab:ital,wght@0,600;0,700;1,700&display=swap" rel="stylesheet">
<style>
  :root {
    --red: #e3262a;
    --red-dark: #c81f26;
    --yellow: #fbe95a;
    --blue: #1d4fa6;
    --label-red: #e3262a;
    --paper: #f1f1f2;
    --photo-a: #d9d9db;
    --photo-b: #bfc0c3;
    --box-line: #9ea3a8;
    --lemon-a: #f4eb8a;
    --lemon-b: #e6c62a;
  }
  * { margin: 0; padding: 0; box-sizing: border-box; }
  html, body { width: 1008px; height: 1200px; overflow: hidden; background: #fff; }
  .flyer { position: relative; width: 1008px; height: 1200px; background: var(--paper); overflow: hidden;
    font-family: "Alfa Slab One", serif; color: var(--blue); }

  .header { position: absolute; left: 0; top: 0; width: 1008px; height: 176px;
    background: linear-gradient(90deg, var(--red-dark), var(--red) 50%, var(--red-dark)); text-align: center; }
  .header::after { content: ""; position: absolute; left: 0; bottom: -6px; width: 100%; height: 6px;
    background: linear-gradient(#bbb, #eee); }
  .brand-name { position: absolute; left: 0; right: 0; top: 30px; font-family: "Alfa Slab One", serif;
    font-weight: 400; font-size: 50px; line-height: 60px; letter-spacing: 2px; color: var(--yellow); }
  .brand-name .line2 { display: block; font-size: 26px; line-height: 40px; letter-spacing: 8px; margin-top: 14px; }

  .food-photo { position: absolute; left: 0; top: 182px; width: 1008px; height: 760px;
    background: radial-gradient(ellipse at 50% 55%, var(--photo-b), var(--photo-a) 55%, var(--paper) 85%); opacity: .75; }
  .lower-swoosh { position: absolute; left: 0; top: 900px; }

  .block { position: absolute; }
  .heading { font-family: "Alfa Slab One", serif; font-weight: 400; font-size: 20px; line-height: 26px; color: var(--blue); white-space: nowrap; }
  .tagline { font-family: "Zilla Slab", serif; font-style: italic; font-weight: 700; font-size: 21px; line-height: 26px; color: var(--red); white-space: nowrap; }
  .list { list-style: none; font-weight: 400; font-size: 13px; line-height: 31px; white-space: nowrap; }
  .label { font-weight: 400; font-size: 13px; line-height: 31px; color: var(--label-red); }
  .multi { line-height: 16px; padding: 7px 0 8px; }
  .note { font-family: "Zilla Slab", serif; font-style: italic; font-weight: 700; font-size: 19px; line-height: 26px; color: var(--red); }

  .menu-box { position: absolute; border: 2px solid var(--box-line); background: rgba(240,241,243,.85); }
  .served { font-family: "Zilla Slab", serif; font-weight: 600; font-size: 14px; line-height: 16px; color: #444; }
  .box-group { margin-bottom: 20px; }
  .sides-box { text-align: center; }
  .sides-box .price-note { font-family: "Zilla Slab", serif; font-weight: 600; font-size: 14px; line-height: 15px; color: #333; }

  .drink-photo { position: absolute; left: 749px; top: 945px; width: 259px; height: 255px;
    background: radial-gradient(ellipse at 45% 55%, var(--lemon-b), var(--lemon-a) 55%, #fbfbf6 85%); }
</style>
</head>
<body>
<div class="flyer">
  <header class="header">
    <h1 class="brand-name">COPPERLEAF KITCHEN<span class="line2">RESTAURANT</span></h1>
  </header>

  <div class="food-photo" role="img" aria-label="Faded photo of a soul food plate with fried chicken and greens"></div>
  <svg class="lower-swoosh" width="1008" height="300" viewBox="0 0 1008 300" aria-hidden="true">
    <path d="M0 40 C 250 10, 700 0, 1008 20 L1008 300 L0 300 Z" fill="#fbfbfb"/>
  </svg>

  <div class="block" style="left:77px; top:223px;">
    <h2 class="heading">START YOUR DAY WITH US!</h2>
    <p class="tagline">Breakfast starting at 6am</p>
  </div>
  <ul class="block list" style="left:77px; top:290px;">
    <li>EGGS - 1.99</li>
    <li>SAUSAGE PATTIES - 2 for 1.99</li>
    <li>SMOKED LINK SAUSAGE - 2 for 1.99</li>
    <li>HASHBROWNS - 1.99</li>
    <li>BISCUSITS - 1.99</li>
    <li>BAKED HAM - 1.99</li>
    <li>BACON - 1.99</li>
    <li>PAN CAKE - 1.99</li>
    <li>SANDWICHES - 2.99</li>
  </ul>

  <div class="block" style="left:466px; top:223px;">
    <h2 class="heading">BUFFET Soul Food!</h2>
    <p class="tagline">Create a plate from the line for only 7.99</p>
  </div>
  <div class="block" style="left:466px; top:290px;">
    <p class="label">MAIN:</p>
    <ul class="list">
      <li>RED BEANS &amp; SAUSAGE</li>
      <li>BEEF TIPS</li>
      <li>TURKEY NECKS</li>
      <li>FRIED \ BAKED CHICKEN</li>
      <li>SPAGHETTI</li>
      <li class="multi">STUFFED BELL PEPPER (Shrimp,<br>Crab and Sausage)</li>
      <li>CHICKEN ON A STICK</li>
      <li>BREAD &amp; DRINK OF THE DAY</li>
    </ul>
    <p class="note" style="margin-top:8px;">*Lunch from 11am to 4pm;<br>Dinner from 5pm to 8pm</p>
  </div>
  <div class="block" style="left:779px; top:288px;">
    <p class="label">SIDES:</p>
    <ul class="list">
      <li>RICE</li>
      <li>MAC N CHEESE</li>
      <li>COLLARD GREENS</li>
      <li>BBQ RED BEANS</li>
      <li>MASH POTATOES</li>
      <li>CORN BREAD</li>
      <li>GREEN BEANS</li>
      <li>CORN</li>
      <li>YAMS</li>
      <li>DRESSING</li>
    </ul>
  </div>

  <div class="block" style="left:81px; top:732px;">
    <p class="label">SALADS:</p>
    <ul class="list">
      <li>CHEF SALAD &nbsp;- 7.00</li>
      <li>GRILLED CHICKEN SALAD - 7.50</li>
      <li>POPCORN CHICKEN SALAD - 7.50</li>
    </ul>
    <p class="label" style="margin-top:6px;">BURGERS:</p>
    <ul class="list">
      <li>CLASSIC BURGER - 5.00</li>
      <li>CLASSIC CHEESEBURGER - 6.00</li>
      <li>BACON AND CHEESEBURGER - 7.00</li>
    </ul>
    <p class="label" style="margin-top:9px;">RIBS:</p>
    <ul class="list">
      <li>FULL RACK - 16.99</li>
      <li>HALF RACK - 8.99</li>
    </ul>
  </div>

  <div class="menu-box" style="left:441px; top:685px; width:286px; height:482px; padding:22px 0 0 41px;">
    <div class="box-group">
      <p class="label" style="line-height:16px;">FRIED CHICKEN</p>
      <p class="served">(Served with 2sides)</p>
      <ul class="list"><li>2 PC WHITE - 6.99</li><li>2PC DARK - 4.99</li></ul>
    </div>
    <div class="box-group">
      <p class="label" style="line-height:16px;">STRIPS</p>
      <p class="served">(Served with 2sides)</p>
      <ul class="list"><li>3PC-3.95 MEAL - 5.99</li><li>6PC-7.00 MEAL - 8.99</li><li>9PC-10.99 MEAL - 12.99</li></ul>
    </div>
    <div class="box-group" style="margin-top:24px;">
      <p class="label" style="line-height:16px;">SEA FOOD</p>
      <p class="served">(Served with 2sides)</p>
      <ul class="list"><li>2PC FRIED FISH - 8.99</li><li>6PC SHRIMP - 6.99</li><li>12PC SHRIMP - 11.99</li></ul>
    </div>
  </div>

  <div class="menu-box sides-box" style="left:725px; top:685px; width:227px; height:237px; padding-top:31px;">
    <p class="label" style="line-height:16px;">SIDES</p>
    <p class="price-note">Individual - 2.00 /<br>Large - 4.00</p>
    <ul class="list" style="margin-top:1px;"><li>OKRA</li><li>FRIES</li><li>BROCCOLI</li><li>SIDE SALAD</li></ul>
  </div>

  <div class="drink-photo" role="img" aria-label="Photo of two glasses of iced lemonade with fresh lemon slices"></div>
</div>
</body>
</html>
```